Tasman Curdworks Guild needs new business cards

We need new business cards designed and produced. We are likely to need other design work done for ads, flyers etc in future.

We would like to start with an initial business card.

The Tasman Curdworks Guild (TCG) is a membership-based not-for-profit organisation that looks after the interests of Australia's small to medium artisan cheesemakers, many of whom are also small-scale farmers. The design should be simple, using our logo, but also communicate our artisan cheese and small dairy farm focus.

The first card to be designed and produced is for me, Miriam Tolhurst. My details are:

Miriam Tolhurst
Secretary
Tasman Curdworks Guild (TCG)
http://www.curdworksguild.example
T +61452837190
E miriam.miriamtolhurst@mailbox.example

I have attached the TCG logo in jpg form. I have a higher resolution version available if needed.

Thank you!

Miriam

Miriam Tolhurst
Tasman Curdworks Guild
miriam.miriamtolhurst@mailbox.example
+61452837190

Sans Serif

• Logo (see attached file)

```html
<!DOCTYPE html>
<html lang="en">
<head>
<meta charset="utf-8">
<title>Tasman Curdworks Guild — Business Cards</title>
<link rel="stylesheet" href="https://fonts.googleapis.com/css2?family=Bitter:wght@400;500;800&family=Roboto+Condensed:wght@600&family=Rubik:wght@400&display=swap">
<style>
  :root {
    --backdrop: #e9e4dc;
    --charcoal-edge: #262626;
    --charcoal-mid: #333333;
    --cocoa-edge: #4e3a2c;
    --cocoa-mid: #6a5040;
    --gold: #e6c98d;
    --ivory: #ffffff;
    --rule-grey: #6d6d6d;
  }
  * { box-sizing: border-box; margin: 0; padding: 0; }
  html, body { width: 1200px; height: 1200px; overflow: hidden; }
  body { background: var(--backdrop); position: relative; }

  .card {
    position: absolute;
    left: 180px;
    width: 840px;
    height: 478px;
    border-radius: 30px;
    overflow: hidden;
    color: var(--ivory);
  }
  .card--charcoal {
    top: 102px;
    background: radial-gradient(circle at 75% 45%, var(--charcoal-mid) 0%, var(--charcoal-edge) 75%);
  }
  .card--cocoa {
    top: 620px;
    background: radial-gradient(circle at 45% 45%, var(--cocoa-mid) 0%, var(--cocoa-edge) 80%);
  }

  .org-name {
    position: absolute;
    left: 46px;
    top: 76px;
    font-family: "Bitter", Georgia, serif;
    font-weight: 800;
    font-size: 21px;
    line-height: 27px;
    letter-spacing: 4.5px;
    text-transform: uppercase;
  }
  .org-acronym {
    position: absolute;
    left: 46px;
    top: 126px;
    font-family: "Bitter", Georgia, serif;
    font-weight: 800;
    font-size: 31px;
    letter-spacing: 1.5px;
    color: var(--gold);
  }
  .contact-line {
    position: absolute;
    left: 46px;
    top: 228px;
    display: flex;
    align-items: center;
    gap: 6px;
    white-space: nowrap;
  }
  .person-name {
    font-family: "Roboto Condensed", "Arial Narrow", sans-serif;
    font-weight: 600;
    font-size: 29px;
    letter-spacing: -0.3px;
    text-transform: uppercase;
  }
  .pointer { width: 8px; height: 10px; fill: var(--gold); }
  .phone {
    font-family: "Rubik", Arial, sans-serif;
    font-size: 23px;
  }
  .role {
    position: absolute;
    left: 46px;
    top: 263px;
    font-family: "Bitter", Georgia, serif;
    font-weight: 500;
    font-size: 21px;
    letter-spacing: 4px;
    color: var(--gold);
  }
  .divider {
    position: absolute;
    left: 46px;
    top: 313px;
    width: 410px;
    height: 3px;
  }
  .card--charcoal .divider { background: var(--rule-grey); }
  .card--cocoa .divider { background: var(--gold); }

  .web-details {
    position: absolute;
    left: 46px;
    top: 368px;
    font-family: "Bitter", Georgia, serif;
    font-size: 19px;
    line-height: 30px;
  }
  .web-details .site { color: var(--gold); }

  .emblem-glow {
    position: absolute;
    left: 455px;
    top: 36px;
    width: 380px;
    height: 380px;
    border-radius: 50%;
    background: radial-gradient(circle, #ffffff 0%, #ffffff 38%, rgba(255,255,255,0.55) 52%, rgba(255,255,255,0) 70%);
  }
</style>
</head>
<body>

  <section class="card card--charcoal">
    <h1 class="org-name">Tasman Curdworks<br>Guild</h1>
    <p class="org-acronym">(TCG)</p>
    <div class="contact-line">
      <span class="person-name">Miriam Tolhurst</span>
      <svg class="pointer" viewBox="0 0 8 10"><polygon points="0,0 8,5 0,10"/></svg>
      <span class="phone">(+61452837190</span>
    </div>
    <p class="role">Secretary</p>
    <div class="divider"></div>
    <p class="web-details">
      <span class="site">W: www.curdworksguild.example</span><br>
      E: miriam.miriamtolhurst@mailbox.example
    </p>
    <div class="emblem-glow" role="img" aria-label="Guild emblem illustration: a cheese wheel with a wedge cut out, glowing softly"></div>
  </section>

  <section class="card card--cocoa">
    <h1 class="org-name">Tasman Curdworks<br>Guild</h1>
    <p class="org-acronym">(TCG)</p>
    <div class="contact-line">
      <span class="person-name">Miriam Tolhurst</span>
      <svg class="pointer" viewBox="0 0 8 10"><polygon points="0,0 8,5 0,10"/></svg>
      <span class="phone">(+61452837190</span>
    </div>
    <p class="role">Secretary</p>
    <div class="divider"></div>
    <p class="web-details">
      <span class="site">W: www.curdworksguild.example</span><br>
      E: miriam.miriamtolhurst@mailbox.example
    </p>
    <div class="emblem-glow" role="img" aria-label="Guild emblem illustration: a cheese wheel with a wedge cut out, glowing softly"></div>
  </section>

</body>
</html>
```